Looking for fresh and exciting business card design that is simple and yet eye catching and impactfu

I am starting my own independent Marketing Communications consultancy with aim to service a small group of clients. Focus on aviation, travel and hospitality industries. Name of the consultancy is RVB BizLink or RVB Marketing Communications. Basic content of the card will be
RVB Marketing Communications / RVB BizLink
Greta Holm Vasquez
Email
Mobile
Website

Target Market(s)

Aviation, travel and hospitality industries

Industry/Entity Type

Travel

Contact Information for Business Card

Greta Holm Vasquez
Consultant
gretahkv@mailbrook.example
Mobile : +86 1502 846 2071
Skype: gretabluecanvas

Font styles to use
Sans Serif
Script

Requirements
Must have
• Professional look and feel.
Nice to have
• Fresh, contrast. I don't have a logo so using the company name to create a focal point.
Should not have
• Too many colors.

```html
<!DOCTYPE html>
<html lang="en">
<head>
<meta charset="utf-8">
<title>RVB BizLink – Business Card</title>
<link rel="stylesheet" href="https://fonts.googleapis.com/css2?family=Montserrat:wght@700&family=Questrial&display=swap">
<style>
  :root {
    --page-bg: #e9e9e9;
    --card-light: #fbfbfb;
    --card-shade: #dcdee0;
    --brand-blue: #2ba6de;
    --brand-blue-light: #45c0ea;
    --ink-dark: #4a4a4a;
    --ink-mid: #666666;
    --icon-white: #ffffff;
  }
  * { margin: 0; padding: 0; box-sizing: border-box; }
  html, body {
    width: 1200px;
    height: 900px;
    overflow: hidden;
    background: var(--page-bg);
  }
  .card {
    position: absolute;
    left: 100px;
    top: 165px;
    width: 1000px;
    height: 570px;
    overflow: hidden;
    box-shadow: 0 6px 24px rgba(0, 0, 0, 0.15);
  }
  .card-surface {
    position: absolute;
    inset: 0;
    background: linear-gradient(135deg, var(--card-shade) 0%, var(--card-light) 45%, var(--card-shade) 100%);
  }
  .holder-name {
    position: absolute;
    left: 190px;
    top: 62px;
    font-family: "Montserrat", sans-serif;
    font-weight: 700;
    font-size: 42px;
    letter-spacing: 0.5px;
    color: var(--ink-dark);
    white-space: nowrap;
  }
  .holder-role {
    position: absolute;
    left: 180px;
    top: 122px;
    font-family: "Questrial", sans-serif;
    font-size: 36px;
    color: var(--ink-mid);
  }
  .brand {
    position: absolute;
    right: 40px;
    top: 138px;
    display: flex;
    align-items: center;
    gap: 14px;
  }
  .brand-mark {
    width: 52px;
    height: 52px;
    background: var(--brand-blue);
  }
  .brand-name {
    font-family: "Questrial", sans-serif;
    font-size: 40px;
    line-height: 1;
    color: var(--brand-blue);
    white-space: nowrap;
  }
  .bar {
    position: absolute;
    left: 0;
    height: 64px;
    background: linear-gradient(90deg, var(--brand-blue), var(--brand-blue-light));
  }
  .bar-1 { top: 232px; width: 400px; }
  .bar-2 { top: 308px; width: 372px; }
  .bar-3 { top: 384px; width: 344px; }
  .contact-icon {
    position: absolute;
    width: 64px;
    height: 64px;
    background: var(--brand-blue);
  }
  .contact-icon svg { width: 64px; height: 64px; display: block; }
  .icon-email { left: 414px; top: 232px; }
  .icon-phone { left: 386px; top: 308px; }
  .icon-chat  { left: 358px; top: 384px; }
  .contact-text {
    position: absolute;
    font-family: "Questrial", sans-serif;
    font-size: 32px;
    line-height: 64px;
    color: var(--ink-mid);
    white-space: nowrap;
  }
  .text-email { left: 498px; top: 232px; }
  .text-phone { left: 470px; top: 308px; }
  .text-chat  { left: 442px; top: 384px; }
</style>
</head>
<body>
  <div class="card">
    <div class="card-surface" role="img" aria-label="Soft pale grey faceted background texture"></div>

    <div class="holder-name">GRETA HOLM VASQUEZ</div>
    <div class="holder-role">Consultant</div>

    <div class="brand">
      <div class="brand-mark"></div>
      <div class="brand-name">RVB BizLink</div>
    </div>

    <div class="bar bar-1"></div>
    <div class="bar bar-2"></div>
    <div class="bar bar-3"></div>

    <div class="contact-icon icon-email">
      <svg viewBox="0 0 64 64" aria-hidden="true">
        <rect x="14" y="20" width="36" height="24" fill="none" stroke="var(--icon-white)" stroke-width="2.5"/>
        <polyline points="14,20 32,34 50,20" fill="none" stroke="var(--icon-white)" stroke-width="2.5"/>
      </svg>
    </div>
    <div class="contact-icon icon-phone">
      <svg viewBox="0 0 64 64" aria-hidden="true">
        <path d="M24 16 L30 24 L26 29 C28 35 31 38 36 40 L41 36 L48 42 L44 48 C32 48 18 34 18 21 Z" fill="none" stroke="var(--icon-white)" stroke-width="2.5" stroke-linejoin="round"/>
      </svg>
    </div>
    <div class="contact-icon icon-chat"></div>

    <div class="contact-text text-email">gretahkv@mailbrook.example</div>
    <div class="contact-text text-phone">+86 1502 846 2071</div>
    <div class="contact-text text-chat">gretabluecanvas</div>
  </div>
</body>
</html>
```